Book for new dads needs a cover.

We need a cover for a book titled Compass for Rookie Papas: Practical Steps for Surviving the Waiting Months, Juggling Jobs and Home, and Keeping Your Head Steady Before the Little One Arrives. We would like to see a design that emphasizes healthy babies and confident dads.

```html
<!DOCTYPE html>
<html lang="en">
<head>
<meta charset="utf-8">
<title>Compass for Rookie Papas — Cover</title>
<link href="https://fonts.googleapis.com/css2?family=Montserrat:wght@500;600;800&family=Roboto+Slab:wght@400&family=Archivo+Black&display=swap" rel="stylesheet">
<style>
  :root {
    --paper: #ffffff;
    --ink: #1e1e1e;
    --orange: #f7901e;
    --navy: #1f5a96;
    --papa-blue: #1a5a9b;
    --gold: #f2c230;
    --gold-soft: #f6d77a;
    --stache: #3a3a3a;
    --shade: rgba(0,0,0,0.28);
  }
  * { margin: 0; padding: 0; box-sizing: border-box; }
  html, body { width: 1200px; height: 1200px; overflow: hidden; background: var(--paper); }
  .stage { position: relative; width: 1200px; height: 1200px; }
  .cover {
    position: absolute; left: 200px; top: 0; width: 800px; height: 1200px;
    background: var(--paper);
    box-shadow: -6px 0 10px -4px var(--shade), 6px 0 10px -4px var(--shade);
  }
  .author {
    position: absolute; top: 66px; left: 0; width: 100%;
    text-align: center; font-family: "Montserrat", sans-serif; font-weight: 600;
    font-size: 46px; letter-spacing: 14px; color: var(--ink);
  }
  .title-art { position: absolute; left: 0; top: 0; width: 1200px; height: 900px; }
  .title-main { font-family: "Montserrat", sans-serif; font-weight: 800; fill: var(--orange); }
  .title-for { font-family: "Montserrat", sans-serif; font-weight: 500; fill: var(--ink); letter-spacing: 10px; }
  .title-band-text { font-family: "Roboto Slab", serif; fill: #fff; letter-spacing: 16px; }
  .title-papas { font-family: "Archivo Black", sans-serif; fill: var(--papa-blue); }
  .subtitle {
    position: absolute; top: 908px; left: 0; width: 100%;
    text-align: center; font-family: "Montserrat", sans-serif; font-weight: 600;
    font-size: 24px; line-height: 43.5px; letter-spacing: 3px; color: var(--ink);
  }
</style>
</head>
<body>
<div class="stage">
  <div class="cover">
    <div class="author">AUTHOR NAME</div>
    <div class="subtitle">
      PRACTICAL STEPS FOR SURVIVING<br>
      THE WAITING MONTHS, JUGGLING<br>
      JOBS AND HOME, AND KEEPING YOUR<br>
      HEAD STEADY BEFORE THE LITTLE<br>
      ONE ARRIVES
    </div>
  </div>

  <svg class="title-art" viewBox="0 0 1200 900" xmlns="http://www.w3.org/2000/svg">
    <!-- accessory areas sit behind the lettering -->
    <rect x="256" y="604" width="200" height="76" rx="36" fill="var(--gold-soft)" role="img" aria-label="Round gold-framed eyeglasses resting on the first letter"/>
    <rect x="604" y="590" width="118" height="48" rx="8" fill="var(--gold)" role="img" aria-label="Small gold crown with a heart on top of the middle letter"/>
    <rect x="752" y="704" width="236" height="66" rx="32" fill="var(--stache)" role="img" aria-label="Black curled moustache across the last letter"/>

    <text class="title-main" x="608" y="408" font-size="140" text-anchor="middle" textLength="694" lengthAdjust="spacingAndGlyphs">COMPASS</text>

    <line x1="272" y1="453" x2="512" y2="453" stroke="var(--navy)" stroke-width="5" stroke-linecap="round" stroke-dasharray="0 11"/>
    <line x1="692" y1="453" x2="950" y2="453" stroke="var(--navy)" stroke-width="5" stroke-linecap="round" stroke-dasharray="0 11"/>
    <text class="title-for" x="610" y="470" font-size="50" text-anchor="middle">FOR</text>

    <rect x="272" y="484" width="681" height="98" fill="var(--navy)"/>
    <text class="title-band-text" x="620" y="562" font-size="76" text-anchor="middle">ROOKIE</text>

    <text class="title-papas" x="620" y="812" font-size="240" text-anchor="middle" textLength="660" lengthAdjust="spacingAndGlyphs">PAPAS</text>
  </svg>
</div>
</body>
</html>
```